Stationary Design Letterhead and Envelope

Artist should provide Letterhead and envelop stationary designs

Info for stationary:
Fernhallow Outdoor Advertising
4873 Quarry Rd. 915 N. PO BOX 528617
Austin, TX 78519

Dale Fernhallow
President
555-862-1907
dale@fernhallowsigns.example
fernhallowsigns.example

Target Market(s)

clients

Colors
0054AA
0677BA
7BADD7
CADEEF
E8F1F8

Requirements
Must have
• high quality unique eye catching and dynamic

```html
<!DOCTYPE html>
<html lang="en">
<head>
<meta charset="utf-8">
<title>Fernhallow Outdoor Advertising — Stationery</title>
<link rel="stylesheet" href="https://fonts.googleapis.com/css2?family=Open+Sans:ital,wght@0,400;0,600;0,700;1,400&display=swap">
<style>
  :root {
    --backdrop: #c3b499;
    --paper: #ffffff;
    --brand-blue: #0071ad;
    --blue-mid: #00659c;
    --blue-deep: #004f80;
    --blue-fold: #005a91;
    --ink: #000000;
    --text: #222222;
    --shadow: 0 6px 14px rgba(60, 45, 20, 0.28);
  }
  * { box-sizing: border-box; margin: 0; padding: 0; }
  html, body { width: 1200px; height: 819px; overflow: hidden; background: var(--backdrop); }
  body { font-family: "Open Sans", Arial, sans-serif; color: var(--text); }

  .stage {
    position: absolute; left: 0; top: 0;
    width: 2324px; height: 1583px;
    transform: scale(0.51635);
    transform-origin: 0 0;
  }

  .sheet { position: absolute; background: var(--paper); box-shadow: var(--shadow); overflow: hidden; }
  .sheet svg.art { position: absolute; left: 0; top: 0; }

  .wordmark { font-weight: 700; color: var(--ink); line-height: 1; position: absolute; }
  .wordmark .name { display: block; letter-spacing: 1px; }
  .wordmark .tag { display: block; }
  .wordmark--light { color: #ffffff; }

  /* Letterhead */
  .letterhead { left: 160px; top: 110px; width: 944px; height: 1321px; }
  .letterhead .wordmark { left: 50px; top: 92px; }
  .letterhead .wordmark .name { font-size: 52px; }
  .letterhead .wordmark .tag { font-size: 20px; margin-top: 10px; letter-spacing: 2.4px; }

  .contact { position: absolute; font-size: 19px; line-height: 1.2; }
  .contact .person { color: var(--brand-blue); font-weight: 600; }
  .contact .role { font-style: italic; color: var(--text); }
  .contact .row { display: flex; align-items: flex-start; gap: 8px; }
  .contact .icon { width: 20px; height: 20px; fill: var(--brand-blue); flex: none; }

  .letterhead .contact { right: 40px; top: 1048px; text-align: right; }
  .letterhead .contact .person { font-size: 20px; }
  .letterhead .contact .role { margin-bottom: 16px; }
  .letterhead .contact .row { justify-content: flex-end; margin-top: 3px; }
  .letterhead .contact .row .icon { margin-top: 2px; }

  /* Envelope */
  .envelope { position: absolute; left: 1265px; top: 117px; width: 980px; height: 596px; box-shadow: var(--shadow); }
  .envelope .body { position: absolute; left: 0; top: 107px; width: 980px; height: 489px; background: var(--paper); }
  .envelope .flap-text {
    position: absolute; left: 380px; top: 12px; width: 220px;
    transform: rotate(180deg); text-align: center; color: #ffffff;
  }
  .envelope .flap-text .wordmark { position: static; color: #ffffff; margin-bottom: 6px; }
  .envelope .flap-text .wordmark .name { font-size: 17px; }
  .envelope .flap-text .wordmark .tag { font-size: 7px; margin-top: 2px; letter-spacing: 0.8px; }
  .envelope .flap-text .addr { font-size: 10px; line-height: 1.35; }

  .bands { position: absolute; left: 0; bottom: 0; width: 100%; display: flex; }
  .bands span { display: block; height: 100%; }
  .band-1 { background: var(--brand-blue); }
  .band-2 { background: var(--blue-mid); }
  .band-3 { background: var(--blue-deep); }
  .band-4 { background: var(--ink); flex: 1; }

  /* Business cards */
  .card-back { position: absolute; left: 1507px; top: 810px; width: 463px; height: 272px; background: var(--brand-blue); box-shadow: var(--shadow); }
  .card-back .wordmark { left: 0; right: 0; top: 112px; text-align: center; }
  .card-back .wordmark .name { font-size: 30px; }
  .card-back .wordmark .tag { font-size: 12px; margin-top: 6px; letter-spacing: 1.3px; }

  .card-front { left: 1505px; top: 1163px; width: 463px; height: 274px; }
  .card-front .wordmark { left: 22px; top: 50px; }
  .card-front .wordmark .name { font-size: 24px; }
  .card-front .wordmark .tag { font-size: 9px; margin-top: 5px; letter-spacing: 1px; }
  .card-front .contact { left: 22px; top: 102px; font-size: 13px; }
  .card-front .contact .person { font-size: 15px; }
  .card-front .contact .role { font-size: 14px; margin-bottom: 14px; }
  .card-front .contact .row { gap: 4px; margin-top: 2px; line-height: 1.05; }
  .card-front .contact .icon { width: 15px; height: 15px; }
</style>
</head>
<body>
<svg width="0" height="0" style="position:absolute" aria-hidden="true">
  <defs>
    <symbol id="i-phone" viewBox="0 0 24 24"><path d="M6.6 2.5l3 3.6c.5.6.4 1.4-.1 2L8 9.6c1.2 2.7 3.6 5.1 6.4 6.4l1.5-1.5c.6-.5 1.4-.6 2-.1l3.6 3c.6.5.7 1.4.2 2l-1.6 2c-.7.8-1.8 1.1-2.8.7C10.5 20 4 13.5 1.9 6.7c-.3-1 0-2.1.8-2.8l2-1.6c.6-.5 1.5-.4 1.9.2z"/></symbol>
    <symbol id="i-mail" viewBox="0 0 24 24"><path d="M1 4h22v16H1z M3 6v.4l9 7 9-7V6z M3 9v9h18V9l-9 7z" fill-rule="evenodd"/></symbol>
    <symbol id="i-globe" viewBox="0 0 24 24"><path d="M12 1a11 11 0 1 0 0 22 11 11 0 0 0 0-22zm0 2c1.3 1.3 2.3 3.5 2.6 6H9.4C9.7 6.5 10.7 4.3 12 3zM7.4 9H3.3a9 9 0 0 1 5.5-5.4C8 5 7.5 7 7.4 9zm0 2c.1 2 .6 4 1.4 5.4A9 9 0 0 1 3.3 13h4.1v-2zm2 0h5.2v2H9.4v-2zm0 4h5.2c-.3 2.5-1.3 4.7-2.6 6-1.3-1.3-2.3-3.5-2.6-6zm7.2 0h4.1a9 9 0 0 1-5.5 5.4c.8-1.4 1.3-3.4 1.4-5.4zm0-2v-2h4.1v2zm0-4c-.1-2-.6-4-1.4-5.4A9 9 0 0 1 20.7 9z"/></symbol>
    <symbol id="i-pin" viewBox="0 0 24 24"><path d="M12 1a7.5 7.5 0 0 0-7.5 7.5C4.5 14 12 23 12 23s7.5-9 7.5-14.5A7.5 7.5 0 0 0 12 1zm0 10.5a3 3 0 1 1 0-6 3 3 0 0 1 0 6z"/></symbol>
  </defs>
</svg>

<main class="stage">
  <!-- Letterhead -->
  <section class="sheet letterhead">
    <svg class="art" width="944" height="1321" viewBox="0 0 944 1321" aria-hidden="true">
      <rect x="0" y="0" width="944" height="69" fill="var(--brand-blue)"/>
      <polygon points="692,69 944,69 944,125 848,175 800,200" fill="var(--brand-blue)"/>
      <polygon points="800,200 848,175 880,215" fill="var(--blue-fold)"/>
      <polygon points="848,175 944,125 944,296" fill="var(--ink)"/>
    </svg>
    <div class="wordmark"><span class="name">FERNHALLOW</span><span class="tag">OUTDOOR ADVERTISING</span></div>
    <div class="contact">
      <div class="person">Dale Fernhallow</div>
      <div class="role">President</div>
      <div class="row"><span>555-862-1907</span><svg class="icon"><use href="#i-phone"/></svg></div>
      <div class="row"><span>dale@fernhallowsigns.example</span><svg class="icon"><use href="#i-mail"/></svg></div>
      <div class="row"><span>fernhallowsigns.example</span><svg class="icon"><use href="#i-globe"/></svg></div>
      <div class="row"><span>4873 Quarry Rd. 915 N. PO BOX 528617<br>Austin, TX 78519</span><svg class="icon"><use href="#i-pin"/></svg></div>
    </div>
    <div class="bands" style="height:89px">
      <span class="band-1" style="width:162px"></span>
      <span class="band-2" style="width:181px"></span>
      <span class="band-3" style="width:176px"></span>
      <span class="band-4"></span>
    </div>
  </section>

  <!-- Envelope -->
  <section class="envelope">
    <svg class="art" style="position:absolute;left:0;top:0" width="980" height="108" viewBox="0 0 980 108" aria-hidden="true">
      <path d="M18,10 Q20,0 32,0 L950,0 Q962,0 964,10 L980,108 L0,108 Z" fill="var(--brand-blue)"/>
    </svg>
    <div class="flap-text">
      <div class="wordmark"><span class="name">FERNHALLOW</span><span class="tag">OUTDOOR ADVERTISING</span></div>
      <div class="addr">4873 Quarry Rd. 915 N. PO BOX 528617<br>Austin, TX 78519</div>
    </div>
    <div class="body"></div>
    <div class="bands" style="height:94px">
      <span class="band-1" style="width:169px"></span>
      <span class="band-2" style="width:188px"></span>
      <span class="band-3" style="width:185px"></span>
      <span class="band-4"></span>
    </div>
  </section>

  <!-- Business card back -->
  <section class="card-back">
    <div class="wordmark wordmark--light"><span class="name">FERNHALLOW</span><span class="tag">OUTDOOR ADVERTISING</span></div>
  </section>

  <!-- Business card front -->
  <section class="sheet card-front">
    <svg class="art" width="463" height="274" viewBox="0 0 463 274" aria-hidden="true">
      <rect x="0" y="0" width="463" height="33" fill="var(--brand-blue)"/>
      <polygon points="338,33 463,33 463,60 415,87 390,97" fill="var(--brand-blue)"/>
      <polygon points="390,97 415,87 430,104" fill="var(--blue-fold)"/>
      <polygon points="415,87 463,60 463,144" fill="var(--ink)"/>
    </svg>
    <div class="wordmark"><span class="name">FERNHALLOW</span><span class="tag">OUTDOOR ADVERTISING</span></div>
    <div class="contact">
      <div class="person">Dale Fernhallow</div>
      <div class="role">President</div>
      <div class="row"><svg class="icon"><use href="#i-phone"/></svg><span>555-862-1907</span></div>
      <div class="row"><svg class="icon"><use href="#i-mail"/></svg><span>dale@fernhallowsigns.example</span></div>
      <div class="row"><svg class="icon"><use href="#i-globe"/></svg><span>fernhallowsigns.example</span></div>
      <div class="row"><svg class="icon"><use href="#i-pin"/></svg><span>4873 Quarry Rd. 915 N. PO BOX 528617<br>Austin, TX 78519</span></div>
    </div>
    <div class="bands" style="height:25px">
      <span class="band-1" style="width:78px"></span>
      <span class="band-2" style="width:89px"></span>
      <span class="band-3" style="width:88px"></span>
      <span class="band-4"></span>
    </div>
  </section>
</main>
</body>
</html>
```